Corporate-Design für Unternehmensberatung
Zielgruppe
Unternehmensberatung aus Tübingen, spezialisiert auf Change Management, Personalentwicklung und Organisationsentwicklung. Zielgruppe sind international agierende Top-Unternehmen.
Aufgabenstellung
Farbschema:
Hex: # 918f8b Pantone: Cool Gray 8 C
Hex: # 921108 Pantone: 7621 C,
vgl. PDF Datei.
Gerne nur Bildmarke ohne Schriftzug, Schriftzug allerdings nicht ohne Bildmarke zu verwenden.

```html
<!DOCTYPE html>
<html lang="de">
<head>
<meta charset="utf-8">
<title>wendepunkt – Geschäftsausstattung</title>
<link href="https://fonts.googleapis.com/css2?family=Arimo:wght@400;700&display=swap" rel="stylesheet">
<style>
  :root{
    --brand-red:#921108;
    --brand-gray:#918f8b;
    --ink:#1d1d1d;
    --paper:#ffffff;
    --backdrop:#e7e9e8;
    --rule:#2a2a2a;
  }
  *{box-sizing:border-box;margin:0;padding:0}
  html,body{width:1200px;height:924px;overflow:hidden}
  body{background:var(--backdrop);font-family:"Arimo",Arial,sans-serif;color:var(--ink);position:relative}

  .sheet{position:absolute;background:var(--paper);box-shadow:0 2px 10px rgba(0,0,0,.08)}

  /* Letterhead */
  .letterhead{left:640px;top:40px;width:420px;height:594px}
  .fold-mark{position:absolute;left:0;width:10px;border-top:1px solid var(--rule)}
  .fold-mark.top{top:210px}
  .fold-mark.bottom{top:420px}
  .brand{display:flex;align-items:center;gap:6px;color:var(--brand-red);font-weight:400}
  .brand-square{display:inline-block;border:2px solid var(--brand-red)}
  .letterhead .brand{position:absolute;left:56px;top:40px;font-size:15px}
  .letterhead .brand-square{width:14px;height:14px}
  .sender{position:absolute;left:56px;top:66px;font-size:8px;line-height:1.3;width:120px}
  .sender strong{display:block}
  .subject{position:absolute;left:56px;top:150px;font-size:12.5px;width:320px}
  .subject strong{font-weight:700}
  .body-copy{position:absolute;left:56px;top:182px;width:320px;font-size:8px;line-height:1.3}
  .body-copy p{margin-bottom:12px}
  .signature{position:absolute;left:56px;top:350px;width:90px;height:34px;background:linear-gradient(90deg,#f3f3f3,#e6e6e6)}
  .signoff{position:absolute;left:56px;top:388px;font-size:8px}
  .signoff small{display:block;font-size:4.5px;line-height:1.3;margin-top:2px;width:70px}
  .footer-rule{position:absolute;left:0;right:0;border-top:1px solid var(--rule)}
  .footer-rule.upper{top:470px}
  .footer-rule.lower{top:570px}
  .footer-cols{position:absolute;left:56px;right:40px;top:482px;display:flex;justify-content:space-between;font-size:7px;line-height:1.3}
  .footer-cols p{width:95px}

  /* Business cards */
  .card{width:270px;height:172px}
  .card-back{left:110px;top:500px}
  .card-front{left:60px;top:700px}
  .card-back .brand-square{position:absolute;left:38px;top:46px;width:60px;height:60px;border-width:5px}
  .contact{position:absolute;left:130px;top:46px;font-size:8px;line-height:1.35}
  .contact .name{color:var(--brand-red);font-size:11px;margin-bottom:6px}
  .card-front .brand{position:absolute;left:34px;top:62px;font-size:34px;gap:12px}
  .card-front .brand-square{width:36px;height:36px;border-width:4px}
</style>
</head>
<body>

<section class="sheet letterhead" aria-label="Briefbogen">
  <span class="fold-mark top"></span>
  <span class="fold-mark bottom"></span>

  <div class="brand"><span class="brand-square"></span>wendepunkt</div>
  <div class="sender">
    <strong>Lorem ipsum dolor</strong>
    sit amet, consectetuer adipiscing elit. Aenean commodo ligula eget
  </div>

  <h1 class="subject"><strong>Lorem ipsum dolor</strong> sit amet, consectetuer</h1>

  <div class="body-copy">
    <p>Lorem ipsum dolor sit amet, consectetuer adipiscing elit. Aenean commodo ligula eget doadipiscf Lorem ipsum dolor sit amet, consectetuer adipiscing elit. Aenean commodo ligula eget doadipiscf Lorem ipsum dolor sit amet, consectetuer adipiscing elit.</p>
    <p>Lorem ipsum dolor sit amet, consectetuer adipiscing elit. Aenean commodo ligula eget doadipiscf Lorem ipsum dolor sit amet, consectetuer adipiscing elit. Aenean commodo ligula eget doadipiscf</p>
    <p>Lorem ipsum dolor sit amet, consectetuer adipiscing elit. Aenean commodo ligula eget doadipiscf Lorem ipsum dolor sit amet, consectetuer adipiscing elit. Aenean commodo ligula eget doadipiscf</p>
    <p>Lorem ipsum dolor sit amet, consectetuer adipiscing elit. Aenean commodo</p>
  </div>

  <div class="signature" role="img" aria-label="Handschriftliche Unterschrift"></div>
  <div class="signoff">ligula eget doadipiscf
    <small>Lorem ipsum dolor sit amet, consectetuer adipiscing elit. Aenean commodo ligula eget</small>
  </div>

  <span class="footer-rule upper"></span>
  <div class="footer-cols">
    <p>Lorem ipsum dolor sit amet, consectetuer adipiscing elit. Aenean commodo ligula eget doadipiscf</p>
    <p>Lorem ipsum dolor sit amet, consectetuer adipiscing elit. Aenean commodo ligula eget doadipiscf</p>
    <p>Lorem ipsum dolor sit amet, consectetuer adipiscing elit. Aenean commodo ligula eget doadipiscf</p>
  </div>
  <span class="footer-rule lower"></span>
</section>

<section class="sheet card card-back" aria-label="Visitenkarte Rückseite">
  <span class="brand-square"></span>
  <div class="contact">
    <p class="name">Jonas Keller</p>
    <p>T +49 30 5550-128</p>
    <p>F +49 30 5550-129</p>
    <p>M +49 151 55501234</p>
    <p>info@wendepunkt-example.com</p>
    <p>www.wendepunkt-example.de</p>
  </div>
</section>

<section class="sheet card card-front" aria-label="Visitenkarte Vorderseite">
  <div class="brand"><span class="brand-square"></span>wendepunkt</div>
</section>

</body>
</html>
```